Kettle Ledger Business Card design

We need a stand out business card design for Accounting practice based in Australia specialising in pubs, clubs and hotels. We help venues maximise margins, create time and manage cashflow. One club we have been working with for the last 6 months has increased revenue by 3% and margin by 5% in this time frame. We have a back office outsourced system that costs less than having a full time employee and also allows the venues the added benefit of:<br/>-using the office space to become a revenue generating opportunity. <br/>-a complete system to enhance governance, accountability and efficiency within their operation<br/>-52 weeks cover so no hassle to cover annual/sick .. leave<br/><br/>We would like to see designs that use the colours of our logo (green & blue).
Target Market(s)
Australian Pubs, Clubs & Hotels abookkeeping, accounting and tax services
Industry/Entity Type
Accountant
Contact Information for Business Card
Miriam Oakley CPA
Principal
Accountant Tax Agent
Miriam@KettleLedger-example.com.au
0418693142
www.kettleledger-example.com.au
Accounting / Payroll / Tax / SMSF / Technology
Colors
Designer to choose colors to be used in the design.
Look and feel
Each slider illustrates characteristics of the customer's brand and the style your logo design should communicate.

```html
<!DOCTYPE html>
<html lang="en">
<head>
<meta charset="utf-8">
<title>Kettle Ledger Business Card</title>
<link rel="stylesheet" href="https://fonts.googleapis.com/css2?family=Work+Sans:wght@400;500;700&family=Libre+Baskerville:wght@700&display=swap">
<style>
  :root {
    --stage: #8f8d8e;
    --card-green: #4c8c5f;
    --card-paper: #efefed;
    --brand-blue: #2f4fa3;
    --brand-green: #1f8048;
    --ink-white: #ffffff;
    --motif-blue: #3552a6;
    --motif-green: #208a4e;
  }
  * { box-sizing: border-box; margin: 0; padding: 0; }
  html, body { width: 1200px; height: 880px; overflow: hidden; }
  body {
    background: var(--stage);
    position: relative;
    font-family: "Work Sans", Arial, sans-serif;
  }
  .card {
    position: absolute;
    width: 620px;
    height: 354px;
    overflow: hidden;
    box-shadow: 0 6px 18px rgba(0,0,0,0.25);
  }
  /* Back side */
  .card-back {
    left: 110px; top: 60px;
    background: var(--card-green);
    color: var(--ink-white);
  }
  .wordmark {
    position: absolute;
    display: flex;
    align-items: center;
    gap: 14px;
    font-weight: 700;
    letter-spacing: -0.5px;
  }
  .wordmark-dot { border-radius: 50%; flex: none; }
  .card-back .wordmark { left: 150px; top: 120px; font-size: 48px; }
  .card-back .wordmark-dot { width: 30px; height: 30px; background: var(--ink-white); }
  .services {
    position: absolute;
    left: 0; right: 0; bottom: 52px;
    text-align: center;
    font-family: "Libre Baskerville", Georgia, serif;
    font-weight: 700;
    font-size: 17px;
    letter-spacing: 0.5px;
  }
  /* Front side */
  .card-front {
    left: 470px; top: 466px;
    background: var(--card-paper);
  }
  .card-front .wordmark { left: 36px; top: 44px; font-size: 34px; color: var(--brand-blue); }
  .card-front .wordmark-dot { width: 22px; height: 22px; background: var(--brand-green); }
  .brand-motif {
    position: absolute;
    left: 60px; top: 190px;
    width: 320px; height: 320px;
    border-radius: 50%;
    background: linear-gradient(135deg, var(--motif-blue) 0%, var(--motif-blue) 45%, var(--motif-green) 100%);
  }
  .contact {
    position: absolute;
    right: 30px; top: 34px;
    text-align: right;
    font-size: 15px;
    line-height: 1.35;
  }
  .contact-name { color: var(--brand-blue); font-weight: 700; font-size: 21px; }
  .contact-role { color: var(--brand-green); font-size: 15px; }
  .contact-lines { margin-top: 22px; color: var(--brand-blue); }
  .contact-line { display: flex; justify-content: flex-end; align-items: center; gap: 8px; height: 26px; }
  .contact-line svg { width: 16px; height: 16px; flex: none; }
</style>
</head>
<body>
  <section class="card card-back" aria-label="Card back">
    <div class="wordmark"><span class="wordmark-dot"></span><span>Kettle Ledger</span></div>
    <p class="services">Accounting / Payroll / Tax / SMSF / Technology</p>
  </section>

  <section class="card card-front" aria-label="Card front">
    <div class="wordmark"><span class="wordmark-dot"></span><span>Kettle Ledger</span></div>
    <div class="brand-motif" role="img" aria-label="Large blue and green brand motif"></div>
    <div class="contact">
      <div class="contact-name">Miriam Oakley CPA</div>
      <div class="contact-role">Principal</div>
      <div class="contact-role">Accountant Tax Agent</div>
      <div class="contact-lines">
        <div class="contact-line"><span>0418-693-142</span>
          <svg viewBox="0 0 16 16" aria-hidden="true"><path fill="#1f8048" d="M3 1h3l1.5 4-2 1.3a8 8 0 0 0 4.2 4.2L11 8.5l4 1.5v3a2 2 0 0 1-2 2C7 15 1 9 1 3a2 2 0 0 1 2-2z"/></svg></div>
        <div class="contact-line"><span>www.kettleledger-example.com.au</span>
          <svg viewBox="0 0 16 16" aria-hidden="true"><circle cx="8" cy="8" r="6.5" fill="none" stroke="#1f8048" stroke-width="1.5"/><path d="M1.5 8h13M8 1.5c-3 3.5-3 9.5 0 13M8 1.5c3 3.5 3 9.5 0 13" fill="none" stroke="#1f8048" stroke-width="1.2"/></svg></div>
        <div class="contact-line"><span>Miriam@KettleLedger-example.com.au</span>
          <svg viewBox="0 0 16 16" aria-hidden="true"><rect x="1" y="3" width="14" height="10" fill="#1f8048"/><path d="M1 3l7 6 7-6" fill="none" stroke="#efefed" stroke-width="1.3"/></svg></div>
      </div>
    </div>
  </section>
</body>
</html>
```